Design an App Mockup for a Restaurant discount lottery system

Updated brief:

Choose between these 2:
1- The user picks from 30 different envelopes numbered 1 - 30. The one the user selected should come to the front of the app mockup, and alert a user that he has won a free entree at a restaurant.

2- The user spins a wheel similar to ribbon riches hour, the one he lands on gives alerts the user that he has won a free entree at a restaurant.

```html
<!DOCTYPE html>
<html lang="en">
<head>
<meta charset="UTF-8">
<title>Try Your Luck – Spin Screen</title>
<link href="https://fonts.googleapis.com/css2?family=Arimo:wght@400;700&display=swap" rel="stylesheet">
<style>
  :root {
    --screen-black: #050505;
    --panel-brown: #221c14;
    --panel-brown-light: #2e261b;
    --band-tan: #a59679;
    --header-text: #f4efe2;
    --gold-light: #f6dc8a;
    --gold: #e2b24a;
    --gold-deep: #a9741c;
    --ring-red: #7a1a14;
    --disc-stone: #c9c1a8;
    --disc-stone-dark: #8e866f;
    --ink: #1a1a1a;
    --icon-muted: #3a3226;
    --status-text: #e8e8e8;
  }
  * { margin: 0; padding: 0; box-sizing: border-box; }
  html, body {
    width: 1200px;
    height: 2400px;
    overflow: hidden;
    background: var(--screen-black);
  }
  .app-screen {
    position: relative;
    width: 1200px;
    height: 2400px;
    background: var(--screen-black);
    font-family: "Arimo", Arial, sans-serif;
  }
  .app-screen svg { position: absolute; left: 0; top: 0; }
  .status-text { font-family: "Arimo", Arial, sans-serif; font-weight: 700; fill: var(--status-text); font-size: 44px; }
  .header-title { font-family: "Arimo", Arial, sans-serif; font-weight: 700; fill: var(--header-text); font-size: 57px; letter-spacing: 1px; }
  .arch-label { font-family: "Arimo", Arial, sans-serif; font-weight: 700; fill: #fff7dc; font-size: 70px; letter-spacing: 6px; }
  .spin-label { font-family: "Arimo", Arial, sans-serif; font-weight: 700; fill: var(--ink); font-size: 96px; letter-spacing: 8px; }
  .prize-text { font-family: "Arimo", Arial, sans-serif; font-weight: 700; fill: var(--ink); font-size: 56px; }
</style>
</head>
<body>
<main class="app-screen">
<svg width="1200" height="2400" viewBox="0 0 1200 2400" xmlns="http://www.w3.org/2000/svg">
  <defs>
    <linearGradient id="goldBar" x1="0" y1="0" x2="0" y2="1">
      <stop offset="0" stop-color="var(--gold-light)"/>
      <stop offset="0.5" stop-color="var(--gold)"/>
      <stop offset="1" stop-color="var(--gold-deep)"/>
    </linearGradient>
    <radialGradient id="stoneDisc" cx="0.45" cy="0.35" r="0.7">
      <stop offset="0" stop-color="#e4dfcc"/>
      <stop offset="1" stop-color="var(--disc-stone-dark)"/>
    </radialGradient>
    <linearGradient id="panelShade" x1="0" y1="0" x2="0" y2="1">
      <stop offset="0" stop-color="var(--panel-brown-light)"/>
      <stop offset="1" stop-color="var(--panel-brown)"/>
    </linearGradient>
    <linearGradient id="ornamentTone" x1="0" y1="0" x2="1" y2="1">
      <stop offset="0" stop-color="#3d3324" stop-opacity="0.7"/>
      <stop offset="1" stop-color="#3d3324" stop-opacity="0.15"/>
    </linearGradient>
    <path id="archCurve" d="M190,600 Q598,330 1010,600"/>
  </defs>

  <!-- status bar -->
  <g class="status-bar">
    <rect x="40" y="38" width="8" height="12" fill="var(--status-text)"/>
    <rect x="54" y="32" width="8" height="18" fill="var(--status-text)"/>
    <rect x="68" y="26" width="8" height="24" fill="var(--status-text)"/>
    <rect x="82" y="20" width="8" height="30" fill="#777"/>
    <text class="status-text" x="100" y="52">Nimbus</text>
    <text class="status-text" x="598" y="52" text-anchor="middle">9:59 AM</text>
    <circle cx="925" cy="37" r="16" fill="var(--status-text)"/>
    <text class="status-text" x="955" y="52">51 %</text>
    <rect x="1080" y="20" width="68" height="34" rx="5" fill="none" stroke="var(--status-text)" stroke-width="4"/>
    <rect x="1086" y="26" width="30" height="22" fill="var(--status-text)"/>
    <rect x="1150" y="30" width="6" height="14" fill="var(--status-text)"/>
  </g>

  <!-- game panel -->
  <rect class="game-panel" x="0" y="207" width="1200" height="1430" fill="url(#panelShade)"/>
  <rect x="0" y="740" width="1200" height="8" fill="#15110b"/>
  <rect x="0" y="1270" width="1200" height="8" fill="#15110b"/>
  <rect x="0" y="1637" width="1200" height="763" fill="var(--screen-black)"/>

  <!-- flourish ornaments (flat placeholders) -->
  <rect role="img" aria-label="Faint floral flourish ornament" x="100" y="320" width="230" height="240" rx="40" fill="url(#ornamentTone)"/>
  <rect role="img" aria-label="Faint floral flourish ornament" x="870" y="320" width="230" height="240" rx="40" fill="url(#ornamentTone)"/>
  <rect role="img" aria-label="Faint floral flourish ornament" x="100" y="1380" width="230" height="240" rx="40" fill="url(#ornamentTone)"/>
  <rect role="img" aria-label="Faint floral flourish ornament" x="870" y="1380" width="230" height="240" rx="40" fill="url(#ornamentTone)"/>

  <!-- restaurant header -->
  <g class="restaurant-header">
    <rect x="86" y="207" width="1114" height="89" fill="var(--band-tan)"/>
    <circle cx="156" cy="250" r="89" fill="var(--header-text)"/>
    <circle cx="156" cy="250" r="70" fill="var(--band-tan)"/>
    <text class="header-title" x="309" y="272">RESTAURANT NAME</text>
  </g>

  <!-- wheel -->
  <g class="prize-wheel">
    <circle cx="598" cy="1001" r="560" fill="#120e09"/>
    <rect x="150" y="940" width="900" height="125" fill="url(#goldBar)"/>
    <rect x="1040" y="940" width="40" height="125" fill="url(#goldBar)"/>
    <circle cx="598" cy="1001" r="490" fill="#1c1710"/>
    <circle cx="598" cy="1001" r="480" fill="var(--ring-red)"/>
    <circle cx="598" cy="1001" r="453" fill="none" stroke="url(#goldBar)" stroke-width="50"/>
    <circle cx="598" cy="1001" r="453" fill="none" stroke="var(--ring-red)" stroke-width="50" stroke-dasharray="4 67.15"/>
    <circle cx="598" cy="1001" r="428" fill="var(--ring-red)"/>
    <circle cx="598" cy="1001" r="420" fill="url(#stoneDisc)"/>
    <circle cx="598" cy="1001" r="270" fill="none" stroke="var(--ink)" stroke-width="10"/>
    <circle cx="598" cy="1001" r="255" fill="#b8b099"/>
    <ellipse cx="560" cy="870" rx="120" ry="70" fill="#ffffff" opacity="0.18"/>
    <rect x="534" y="1510" width="127" height="48" fill="var(--disc-stone-dark)"/>
  </g>

  <!-- try your luck arch -->
  <g class="luck-arch">
    <path d="M118,560 Q598,260 1072,560 L1060,660 Q598,400 130,660 Z" fill="url(#goldBar)" stroke="var(--gold-deep)" stroke-width="6"/>
    <text class="arch-label" text-anchor="middle"><textPath href="#archCurve" startOffset="50%">TRY YOUR LUCK</textPath></text>
  </g>

  <!-- spin button -->
  <g class="spin-button">
    <path d="M360,952 L940,952 L980,1000 L1120,1048 L980,1096 L940,1145 L360,1145 L325,1100 L325,997 Z" fill="url(#goldBar)" stroke="var(--gold-deep)" stroke-width="6"/>
    <text class="spin-label" x="640" y="1082" text-anchor="middle">SPIN!</text>
  </g>

  <!-- prize message -->
  <g class="prize-message">
    <rect x="86" y="1669" width="1024" height="207" rx="14" fill="url(#goldBar)"/>
    <rect x="104" y="1687" width="988" height="171" fill="#ffffff"/>
    <text class="prize-text" x="598" y="1758" text-anchor="middle">You won</text>
    <text class="prize-text" x="598" y="1828" text-anchor="middle">a free entree at a restaurant!</text>
  </g>

  <!-- bottom icons -->
  <g class="menu-icon" fill="var(--icon-muted)">
    <rect x="100" y="1980" width="150" height="20"/>
    <rect x="100" y="2025" width="120" height="20"/>
    <rect x="100" y="2070" width="90" height="20"/>
  </g>
  <g class="refresh-icon">
    <path d="M1024,1985 A52,52 0 1 0 1076,2037" fill="none" stroke="var(--icon-muted)" stroke-width="28"/>
    <path d="M1050,1960 L1100,2010 L1040,2015 Z" fill="var(--icon-muted)"/>
  </g>
</svg>
</main>
</body>
</html>
```